Business card to be used as a flyer

This business card should do the trick of a full scale flyer , so basicaly from the business card itself we only keep the size and remove the clasical name , position , company name (etc).
This business cards should be , like said above, used as promo tool, being gived to different girls . So base one : the design is girls oriented.
Colors : black background . We will use gold (color) folio for the text.
Attached you have our logo, but this should not be a proiminent part of the design . You can use only the cat head instead.
Target Market(s)
Girls / Women
Contact Information for Business Card
> black background , gold / folio text and elements
> cat head from the logo in a creative way do be displayed
> proieminent text "your path to success starts here"
> contact details phone and website .
www.velmastrand.ro (website) and 0742163958 (phone)

```html
<!DOCTYPE html>
<html lang="en">
<head>
<meta charset="utf-8">
<title>Velmastrand – Promo Card</title>
<link rel="stylesheet" href="https://fonts.googleapis.com/css2?family=Dancing+Script:wght@700&family=Montserrat:wght@400;500&display=swap">
<style>
  :root {
    --backdrop: #2a2a2a;
    --card: #0b0b0b;
    --card-edge: #1a1a1a;
    --gold: #d4a93a;
    --gold-light: #f0cf6a;
    --gold-deep: #a77b1e;
  }
  * { margin: 0; padding: 0; box-sizing: border-box; }
  html, body {
    width: 1200px;
    height: 1200px;
    overflow: hidden;
    background: var(--backdrop);
  }
  .canvas {
    position: relative;
    width: 1200px;
    height: 1200px;
    display: flex;
    flex-direction: column;
    align-items: center;
    justify-content: center;
    gap: 60px;
  }
  .card {
    position: relative;
    width: 880px;
    height: 500px;
    background: var(--card);
    border: 1px solid var(--card-edge);
    border-radius: 26px;
    overflow: hidden;
  }
  .gold-text {
    background: linear-gradient(100deg, var(--gold-deep) 0%, var(--gold-light) 35%, var(--gold) 60%, var(--gold-deep) 100%);
    -webkit-background-clip: text;
    background-clip: text;
    color: transparent;
  }
  .card-front .brand-name {
    position: absolute;
    left: 0;
    right: 0;
    top: 210px;
    text-align: center;
    font-family: "Montserrat", sans-serif;
    font-weight: 500;
    font-size: 40px;
    letter-spacing: 6px;
  }
  .card-back .tagline {
    position: absolute;
    left: 0;
    right: 0;
    top: 150px;
    text-align: center;
    font-family: "Dancing Script", cursive;
    font-weight: 700;
    font-size: 64px;
  }
  .card-back .divider {
    position: absolute;
    left: 60px;
    right: 60px;
    top: 330px;
    height: 1px;
    background: linear-gradient(90deg, var(--gold-deep), var(--gold-light), var(--gold-deep));
  }
  .contact {
    position: absolute;
    display: flex;
    align-items: center;
    gap: 14px;
    font-family: "Montserrat", sans-serif;
    font-weight: 400;
    font-size: 24px;
    color: var(--gold);
  }
  .contact svg { width: 24px; height: 24px; }
  .contact-phone { left: 60px; top: 360px; }
  .contact-web { right: 60px; top: 420px; }
</style>
</head>
<body>
  <main class="canvas">
    <section class="card card-front">
      <p class="brand-name gold-text">Velmastrand</p>
    </section>

    <section class="card card-back">
      <h1 class="tagline gold-text">Your path to success starts here</h1>
      <div class="divider"></div>

      <div class="contact contact-phone">
        <svg viewBox="0 0 24 24" aria-hidden="true">
          <path fill="var(--gold)" d="M6.6 10.8a15.1 15.1 0 0 0 6.6 6.6l2.2-2.2a1 1 0 0 1 1-.25 11.4 11.4 0 0 0 3.6.57 1 1 0 0 1 1 1V20a1 1 0 0 1-1 1A17 17 0 0 1 3 4a1 1 0 0 1 1-1h3.5a1 1 0 0 1 1 1c0 1.25.2 2.45.57 3.57a1 1 0 0 1-.25 1z"/>
        </svg>
        <span>0742163958</span>
      </div>

      <div class="contact contact-web">
        <svg viewBox="0 0 24 24" aria-hidden="true" fill="none" stroke="var(--gold)" stroke-width="1.6">
          <circle cx="12" cy="12" r="9.5"/>
          <ellipse cx="12" cy="12" rx="4.2" ry="9.5"/>
          <line x1="2.5" y1="12" x2="21.5" y2="12"/>
          <line x1="4" y1="7" x2="20" y2="7"/>
          <line x1="4" y1="17" x2="20" y2="17"/>
        </svg>
        <span>www.velmastrand.ro</span>
      </div>
    </section>
  </main>
</body>
</html>
```